brenwick carpentry business card 2.0

id like to get some extra info added to my current business card ,but i am also open to a new design as well ,id like it to be a clean professional look
i have attached the original card files, i have also attached the crestline trades logo and licensed builder logo that id like to add to all the current info on the old card
also the color green is important as seen in the company logo

Industry/Entity Type

Carpentry

Colors
9bcb3c

```html
<!DOCTYPE html>
<html lang="en">
<head>
<meta charset="UTF-8">
<title>Brenwick Carpentry – Business Card</title>
<link href="https://fonts.googleapis.com/css2?family=Montserrat:wght@400;500;600&display=swap" rel="stylesheet">
<style>
  :root {
    --green: #9bcb3c;
    --charcoal: #2b2b2b;
    --ink: #1a1a1a;
    --paper: #ffffff;
    --backdrop: #e6e6e6;
    --badge-blue: #1d4f91;
  }
  * { box-sizing: border-box; margin: 0; padding: 0; }
  html, body { width: 1200px; height: 794px; overflow: hidden; }
  body {
    background: var(--backdrop);
    font-family: "Montserrat", sans-serif;
    position: relative;
  }
  .card {
    position: absolute;
    top: 248px;
    width: 520px;
    height: 297px;
    border-radius: 3px;
    box-shadow: 0 6px 18px rgba(0,0,0,0.15);
    overflow: hidden;
  }
  .card--front { left: 60px; background: var(--charcoal); }
  .card--back { left: 620px; background: var(--paper); }

  .wordmark {
    display: flex;
    align-items: center;
    gap: 10px;
    font-weight: 500;
    letter-spacing: 0.04em;
    text-transform: uppercase;
    line-height: 1;
  }
  .wordmark__square { width: 10px; height: 10px; background: currentColor; }
  .card--front .wordmark {
    color: var(--paper);
    position: absolute;
    left: 50%; top: 50%;
    transform: translate(-50%, -50%);
    font-size: 30px;
    white-space: nowrap;
  }
  .card--back .wordmark {
    color: var(--ink);
    position: absolute;
    left: 38px; top: 40px;
    font-size: 24px;
  }

  .person { position: absolute; left: 38px; top: 112px; }
  .person__name { font-size: 19px; font-weight: 600; color: var(--ink); }
  .person__title { font-size: 12px; color: var(--ink); margin-top: 4px; }
  .person__rule { width: 26px; height: 2px; background: var(--green); margin-top: 12px; }

  .contact { position: absolute; left: 38px; top: 190px; list-style: none; }
  .contact__item {
    display: flex; align-items: center; gap: 12px;
    font-size: 12px; color: var(--ink); height: 20px;
  }
  .contact__item svg { width: 14px; height: 14px; flex: none; }
  .contact__item strong { font-weight: 600; }

  .badges { position: absolute; right: 30px; bottom: 34px; display: flex; align-items: flex-end; gap: 14px; }
  .badge--square { width: 42px; height: 46px; background: var(--badge-blue); }
  .badge--round { width: 62px; height: 62px; border-radius: 50%; background: var(--green); opacity: 0.85; }

  .card__band { position: absolute; left: 0; right: 0; bottom: 0; height: 8px; background: var(--green); }
</style>
</head>
<body>
  <section class="card card--front" aria-label="Card front">
    <div class="wordmark"><span class="wordmark__square"></span>Brenwick Carpentry</div>
  </section>

  <section class="card card--back" aria-label="Card back">
    <div class="wordmark"><span class="wordmark__square"></span>Brenwick Carpentry</div>

    <div class="person">
      <p class="person__name">Daniel Marsh</p>
      <p class="person__title">Director Brenwick Carpentry Ltd</p>
      <div class="person__rule"></div>
    </div>

    <ul class="contact">
      <li class="contact__item">
        <svg viewBox="0 0 16 16" fill="none" stroke="#9bcb3c" stroke-width="1.4"><path d="M3 2h3l1.5 3.5-2 1.2a8 8 0 0 0 3.8 3.8l1.2-2L14 10v3a1 1 0 0 1-1 1A11 11 0 0 1 2 3a1 1 0 0 1 1-1z"/></svg>
        02109847561
      </li>
      <li class="contact__item">
        <svg viewBox="0 0 16 16" fill="none" stroke="#9bcb3c" stroke-width="1.4"><rect x="1.5" y="3.5" width="13" height="9"/><path d="M1.5 3.5 8 9l6.5-5.5"/></svg>
        daniel@brenwickcarpentry.co.nz
      </li>
      <li class="contact__item">
        <svg viewBox="0 0 16 16" fill="none" stroke="#9bcb3c" stroke-width="1.4"><circle cx="8" cy="8" r="6.5"/><path d="M1.5 8h13M8 1.5c-3 3.5-3 9.5 0 13M8 1.5c3 3.5 3 9.5 0 13"/></svg>
        <span>www.<strong>brenwickcarpentry</strong>.co.nz</span>
      </li>
    </ul>

    <div class="badges">
      <div class="badge badge--square" role="img" aria-label="Crestline Trades membership badge"></div>
      <div class="badge badge--round" role="img" aria-label="Licensed builder certification badge"></div>
    </div>

    <div class="card__band"></div>
  </section>
</body>
</html>
```